Financial Advisor needs waiting room sign

I am a financial advisor that works with a number of accountants to develop prospects. I am looking for a 18"x24" sign to hang in their office waiting rooms to help develop prospect interest in my services. My original idea was to list all of our services in a jumbled way on the sign and on the bottom have something like "Confused? We have the answers?" "Questions - We have answers" Our logo on the bottom. While I think this is still a good idea when I try to design it - it does not work. I am open to other ideas. Here is a list of our services (list in no particular order) and I will attach our logo. List: Vellorin, Vellorin Supplement, Vellorin Advantage, Tolquist, Part A, Part B, Part D, Social Security, Turning 65, Annuities, Fixed Index Annuities, Rollovers, 401k, 403b, Investments, Stock Market, Mutual Funds, Term Insurance, Life Insurance, Final Expense, Long Term Care, Mortgage Protection, 403B / 457 Not for Profit Set Up, 403B / TSA Plans, Annuities, Asset Protection, Charitable Giving, College Funding, Estate Planning, Fixed Indexed Annuities, Guaranteed Income, IRA & 401(K) Assets and Planning, IRA, 401(K), 403(B) Rollovers, Lifetime Income Planning, Retirement Income Planning, Safe Money Options, Social Security, Tactical Asset Allocation

```html
<!DOCTYPE html>
<html lang="en">
<head>
<meta charset="utf-8">
<title>Brackenfield Capital – Waiting Room Sign</title>
<link rel="stylesheet" href="https://fonts.googleapis.com/css2?family=Lato:wght@400;700&family=Source+Sans+3:wght@400;600&display=swap">
<style>
  :root {
    --green: #67a637;
    --green-dark: #4f8a2a;
    --black: #232323;
    --stripe: #0d0d0d;
    --grey-light: #f4f4f4;
    --grey-mid: #d6d6d6;
    --white: #ffffff;
    --ink: #1c1c1c;
  }
  html, body {
    margin: 0;
    padding: 0;
    width: 1040px;
    height: 1200px;
    overflow: hidden;
    background: var(--white);
  }
  .sign {
    display: block;
    width: 1040px;
    height: 1200px;
  }
  .headline { font-family: "Lato", sans-serif; }
  .headline-large { font-size: 84px; font-weight: 400; }
  .headline-sub { font-size: 40px; font-weight: 400; }
  .headline-dark-large { font-size: 86px; font-weight: 400; }
  .headline-dark-sub { font-size: 50px; font-weight: 400; }
  .services-title {
    font-family: "Lato", sans-serif;
    font-weight: 700;
    font-size: 44px;
  }
  .service-item {
    font-family: "Source Sans 3", sans-serif;
    font-size: 26px;
    fill: var(--white);
  }
  .service-tick {
    fill: none;
    stroke: var(--green);
    stroke-width: 3;
    stroke-linecap: round;
    stroke-linejoin: round;
  }
  .brand-name {
    font-family: "Lato", sans-serif;
    font-weight: 700;
    font-size: 44px;
    letter-spacing: 2px;
    fill: var(--green-dark);
  }
</style>
</head>
<body>
<svg class="sign" viewBox="0 0 1040 1200" xmlns="http://www.w3.org/2000/svg" role="img" aria-label="Brackenfield Capital waiting room sign listing services">
  <defs>
    <linearGradient id="wedge-fade" x1="0" y1="0" x2="1" y2="0">
      <stop offset="0" stop-color="var(--grey-mid)"/>
      <stop offset="0.6" stop-color="var(--grey-light)"/>
      <stop offset="1" stop-color="var(--white)"/>
    </linearGradient>
  </defs>

  <!-- background bands -->
  <rect class="band-dark" x="0" y="0" width="1040" height="1058" fill="var(--black)"/>
  <polygon class="band-green-top" points="0,0 1040,0 1040,228 0,77" fill="var(--green)"/>
  <polygon class="band-stripe" points="0,77 1040,228 1040,277 0,80" fill="var(--stripe)"/>
  <polygon class="band-wedge" points="0,80 1040,277 0,423" fill="url(#wedge-fade)"/>
  <polygon class="band-green-lower" points="0,423 1040,277 1040,281 0,465" fill="var(--green)"/>
  <rect class="footer" x="0" y="1058" width="1040" height="142" fill="var(--white)"/>

  <!-- headlines -->
  <text class="headline headline-large" x="1001" y="100" text-anchor="end" fill="var(--white)">Confused?</text>
  <text class="headline headline-sub" x="1001" y="148" text-anchor="end" fill="var(--white)">We have the answers?</text>
  <text class="headline headline-dark-large" x="58" y="253" fill="var(--ink)">Questions?</text>
  <text class="headline headline-dark-sub" x="58" y="311" fill="var(--ink)">We have answers?</text>

  <!-- services -->
  <text class="services-title" x="507" y="459" text-anchor="middle" fill="var(--green)">OUR SERVICES</text>

  <g class="service-column service-column-left">
    <g class="service-ticks" transform="translate(98,0)">
      <path class="service-tick" d="M0,516 l5,8 l9,-16"/>
      <path class="service-tick" d="M0,546 l5,8 l9,-16"/>
      <path class="service-tick" d="M0,576 l5,8 l9,-16"/>
      <path class="service-tick" d="M0,606 l5,8 l9,-16"/>
      <path class="service-tick" d="M0,636 l5,8 l9,-16"/>
      <path class="service-tick" d="M0,666 l5,8 l9,-16"/>
      <path class="service-tick" d="M0,696 l5,8 l9,-16"/>
      <path class="service-tick" d="M0,726 l5,8 l9,-16"/>
      <path class="service-tick" d="M0,756 l5,8 l9,-16"/>
      <path class="service-tick" d="M0,786 l5,8 l9,-16"/>
      <path class="service-tick" d="M0,816 l5,8 l9,-16"/>
      <path class="service-tick" d="M0,846 l5,8 l9,-16"/>
      <path class="service-tick" d="M0,876 l5,8 l9,-16"/>
      <path class="service-tick" d="M0,906 l5,8 l9,-16"/>
      <path class="service-tick" d="M0,936 l5,8 l9,-16"/>
      <path class="service-tick" d="M0,966 l5,8 l9,-16"/>
      <path class="service-tick" d="M0,996 l5,8 l9,-16"/>
    </g>
    <text class="service-item" x="127" y="525">Vellorin</text>
    <text class="service-item" x="127" y="555">Vellorin Supplement</text>
    <text class="service-item" x="127" y="585">Vellorin Advantage</text>
    <text class="service-item" x="127" y="615">Tolquist</text>
    <text class="service-item" x="127" y="645">Part A, Part B, Part D</text>
    <text class="service-item" x="127" y="675">Social Security</text>
    <text class="service-item" x="127" y="705">Turning 65</text>
    <text class="service-item" x="127" y="735">Annuities</text>
    <text class="service-item" x="127" y="765">Fixed Index Annuities</text>
    <text class="service-item" x="127" y="795">Rollovers, 401k, 403b</text>
    <text class="service-item" x="127" y="825">Investments</text>
    <text class="service-item" x="127" y="855">Stock Market</text>
    <text class="service-item" x="127" y="885">Mutual Funds</text>
    <text class="service-item" x="127" y="915">Term Insurance</text>
    <text class="service-item" x="127" y="945">Life Insurance</text>
    <text class="service-item" x="127" y="975">Final Expense</text>
    <text class="service-item" x="127" y="1005">Long Term Care</text>
  </g>

  <g class="service-column service-column-right">
    <g class="service-ticks" transform="translate(522,0)">
      <path class="service-tick" d="M0,516 l5,8 l9,-16"/>
      <path class="service-tick" d="M0,546 l5,8 l9,-16"/>
      <path class="service-tick" d="M0,576 l5,8 l9,-16"/>
      <path class="service-tick" d="M0,606 l5,8 l9,-16"/>
      <path class="service-tick" d="M0,636 l5,8 l9,-16"/>
      <path class="service-tick" d="M0,666 l5,8 l9,-16"/>
      <path class="service-tick" d="M0,696 l5,8 l9,-16"/>
      <path class="service-tick" d="M0,726 l5,8 l9,-16"/>
      <path class="service-tick" d="M0,756 l5,8 l9,-16"/>
      <path class="service-tick" d="M0,786 l5,8 l9,-16"/>
      <path class="service-tick" d="M0,816 l5,8 l9,-16"/>
      <path class="service-tick" d="M0,846 l5,8 l9,-16"/>
      <path class="service-tick" d="M0,876 l5,8 l9,-16"/>
      <path class="service-tick" d="M0,906 l5,8 l9,-16"/>
      <path class="service-tick" d="M0,936 l5,8 l9,-16"/>
      <path class="service-tick" d="M0,966 l5,8 l9,-16"/>
      <path class="service-tick" d="M0,996 l5,8 l9,-16"/>
    </g>
    <text class="service-item" x="557" y="527">Mortgage Protection</text>
    <text class="service-item" x="557" y="557">403B / 457 Not for Profit Set Up</text>
    <text class="service-item" x="557" y="587">403B / TSA Plans</text>
    <text class="service-item" x="557" y="617">Annuities</text>
    <text class="service-item" x="557" y="647">Asset Protection</text>
    <text class="service-item" x="557" y="677">Charitable Giving</text>
    <text class="service-item" x="557" y="707">College Funding</text>
    <text class="service-item" x="557" y="737">Estate Planning</text>
    <text class="service-item" x="557" y="767">Fixed Indexed Annuities</text>
    <text class="service-item" x="557" y="797">Guaranteed Income</text>
    <text class="service-item" x="557" y="827">IRA &amp; 401(K) Assets and Planning</text>
    <text class="service-item" x="557" y="857">IRA 401(K), 403(B) Rollovers</text>
    <text class="service-item" x="557" y="887">Lifetime Income Planning</text>
    <text class="service-item" x="557" y="917">Retirement Income Planning</text>
    <text class="service-item" x="557" y="947">Safe Money Options</text>
    <text class="service-item" x="557" y="977">Social Security</text>
    <text class="service-item" x="557" y="1007">Tactical Asset Allocation</text>
  </g>

  <!-- brand -->
  <g class="brand">
    <circle class="brand-dot" cx="300" cy="1129" r="24" fill="var(--green)"/>
    <text class="brand-name" x="344" y="1144">BRACKENFIELD CAPITAL</text>
  </g>
</svg>
</body>
</html>
```